PowerPoint Template Design

We are an independent private equity and advisory firm (mergers and acquisitions), based in Brazil. We are looking for a power point template to use for companies presentations to investors and other targets (ie competitors).
Find attached the actual template that we use, we need something with this structure but more customized.

- Cover slide with our logo, project name and current date
- Index/Agenda slide
- Content slides
a. Slide with title, subtitle, text and footer. The footer should contain the page number, the person who we are sending to and the word "CONFIDENTIAL"
b. Slide with title, subtitle, text and pictures/charters/graphics
- Final slide with adress and contacts

We do not want something very colorful, we need something plain, simple but modern.

Target Market(s)

Investors, CEOs, CFOs, other advisory firms like DNTallis, DSRH, Almsbury, etc.

Industry/Entity Type

Equity

Requirements
Must have
• - the same colors used by our designer;
- one font only (Century Gothic);

```html
<!DOCTYPE html>
<html lang="en">
<head>
<meta charset="utf-8">
<title>Valen Capital – Project Template – Revised Proposal</title>
<link rel="stylesheet" href="https://fonts.googleapis.com/css2?family=Didact+Gothic&display=swap">
<style>
  :root {
    --slide-bg: #bfbfbf;
    --ink-dark: #7a7a7a;
    --ink-light: #dcdcdc;
    --ink-white: #ffffff;
    --date-ink: #e8e8e8;
    --accent: #ffb000;
    --tab-ink: #5a5a5a;
    --brand-ink: #707070;
  }
  html, body {
    margin: 0;
    padding: 0;
    width: 1200px;
    height: 900px;
    overflow: hidden;
    background: var(--slide-bg);
  }
  .cover-slide {
    position: relative;
    width: 1200px;
    height: 900px;
    background: var(--slide-bg);
    font-family: "Didact Gothic", "Century Gothic", sans-serif;
    overflow: hidden;
  }
  .cover-title {
    position: absolute;
    right: 325px;
    top: 245px;
    margin: 0;
    text-align: right;
    font-weight: 400;
    font-size: 92px;
    line-height: 87px;
    letter-spacing: 5px;
    color: var(--ink-dark);
  }
  .cover-title .firm-dark { color: var(--ink-dark); }
  .cover-title .firm-light { color: var(--ink-light); }
  .cover-title .line { display: block; }
  .cover-subtitle {
    position: absolute;
    right: 322px;
    top: 556px;
    margin: 0;
    font-weight: 400;
    font-size: 43px;
    letter-spacing: 3px;
    word-spacing: -6px;
    color: var(--ink-white);
  }
  .cover-date {
    position: absolute;
    right: 323px;
    top: 617px;
    margin: 0;
    font-size: 22px;
    letter-spacing: 2px;
    color: var(--date-ink);
  }
  .confidential-tab {
    position: absolute;
    left: 1145px;
    top: 258px;
    width: 55px;
    height: 385px;
    background: var(--accent);
    display: flex;
    justify-content: center;
    align-items: center;
  }
  .confidential-tab span {
    writing-mode: vertical-rl;
    text-orientation: mixed;
    font-size: 12px;
    letter-spacing: 15px;
    margin-bottom: -15px;
    color: var(--tab-ink);
  }
  .brand-mark {
    position: absolute;
    right: 52px;
    top: 828px;
    display: flex;
    align-items: center;
    gap: 10px;
    color: var(--brand-ink);
  }
  .brand-mark .brand-square {
    width: 14px;
    height: 14px;
    background: var(--brand-ink);
  }
  .brand-mark .brand-name {
    font-size: 19px;
    letter-spacing: 0;
  }
</style>
</head>
<body>
  <main class="cover-slide">
    <h1 class="cover-title">
      <span class="line"><span class="firm-dark">VALEN</span> <span class="firm-light">CAPITAL</span></span>
      <span class="line">PROJECT</span>
      <span class="line">TEMPLATE</span>
    </h1>
    <p class="cover-subtitle">REVISED PROPOSAL</p>
    <p class="cover-date">MAY 2013</p>

    <div class="confidential-tab"><span>CONFIDENTIAL</span></div>

    <div class="brand-mark">
      <span class="brand-square"></span>
      <span class="brand-name">Valen Capital</span>
    </div>
  </main>
</body>
</html>
```